Email Signatures

I would like to create a new email signature for my team. The design will be the same for everyone, with only individual details such as name and email changing. You can also see our brand style on our website. https://www.tlmbespokehomes.com.au/

Target Market(s)

Clients for new builds or renovations

Industry/Entity Type

Construction

Colors

Designer to choose colors to be used in the design.

```html
<!DOCTYPE html>
<html lang="en">
<head>
<meta charset="UTF-8">
<title>TLM Bespoke Homes – Email Signature</title>
<link href="https://fonts.googleapis.com/css2?family=Exo+2:ital,wght@1,800&family=Poppins:wght@400;500;700&display=swap" rel="stylesheet">
<style>
  :root {
    --page-bg: #bcbcbc;
    --card-bg: #ffffff;
    --brand-green: #0a8f3c;
    --ink: #2d2d2d;
    --photo-tone-a: #cfc7c2;
    --photo-tone-b: #8a7a72;
  }
  * { margin: 0; padding: 0; box-sizing: border-box; }
  html, body { width: 1200px; height: 1200px; overflow: hidden; }
  body { background: var(--page-bg); position: relative; font-family: "Poppins", sans-serif; }

  .signature {
    position: absolute; left: 300px; top: 515px;
    width: 600px; height: 170px; background: var(--card-bg);
  }
  .portrait {
    position: absolute; left: 31px; top: 20px; width: 119px; height: 130px;
    border: 3px solid var(--brand-green);
    background: linear-gradient(160deg, var(--photo-tone-a) 0%, #b9a79c 55%, var(--photo-tone-b) 100%);
  }
  .details { position: absolute; left: 171px; top: 23px; }
  .details__name {
    font-family: "Exo 2", sans-serif; font-style: italic; font-weight: 800;
    font-size: 24.5px; line-height: 1; color: var(--brand-green); letter-spacing: 0.2px;
  }
  .details__role {
    font-size: 17px; font-weight: 500; color: var(--ink); line-height: 1; margin-top: 3px;
  }
  .contact-list { list-style: none; margin-top: 11px; }
  .contact-list li {
    display: flex; align-items: center; gap: 4px;
    font-size: 11.5px; color: var(--ink); height: 17.2px;
  }
  .contact-list svg { width: 13px; height: 13px; fill: var(--brand-green); flex: none; }

  .divider {
    position: absolute; left: 422px; top: 20px; width: 1.5px; height: 131px;
    background: var(--brand-green);
  }
  .brand {
    position: absolute; left: 440px; top: 36px; width: 126px; text-align: center;
    font-weight: 700; font-size: 44px; line-height: 1; color: var(--ink); letter-spacing: 2px;
  }
  .social { position: absolute; left: 468px; top: 116px; display: flex; gap: 7px; }
  .social__link {
    display: block; width: 27px; height: 27px; border-radius: 6px; background: var(--brand-green);
  }
</style>
</head>
<body>
  <section class="signature">
    <div class="portrait" role="img" aria-label="Portrait photo of Dean Whitfield"></div>

    <div class="details">
      <h1 class="details__name">DEAN WHITFIELD</h1>
      <p class="details__role">General Manager</p>
      <ul class="contact-list">
        <li><svg viewBox="0 0 24 24"><path d="M6.6 10.8a15 15 0 006.6 6.6l2.2-2.2c.3-.3.7-.4 1-.2 1.1.4 2.3.6 3.6.6.6 0 1 .4 1 1V20c0 .6-.4 1-1 1A17 17 0 013 4c0-.6.4-1 1-1h3.5c.6 0 1 .4 1 1 0 1.3.2 2.5.6 3.6.1.3 0 .7-.2 1z"/></svg>0400 123 456</li>
        <li><svg viewBox="0 0 24 24"><path d="M2 5h20v14H2z M4 7v.5l8 5.5 8-5.5V7z" fill-rule="evenodd"/></svg>info@tlmbespokehomes.com.au</li>
        <li><svg viewBox="0 0 24 24"><path d="M12 2a7 7 0 00-7 7c0 5 7 13 7 13s7-8 7-13a7 7 0 00-7-7zm0 9.5A2.5 2.5 0 1112 6a2.5 2.5 0 010 5.5z"/></svg>Port Alden, Tasmania, Australia</li>
        <li><svg viewBox="0 0 24 24"><path d="M12 2a10 10 0 100 20 10 10 0 000-20zm6.9 6h-3a15 15 0 00-1.3-3.9A8 8 0 0118.9 8zM12 4c.8 1.2 1.5 2.5 1.9 4h-3.8c.4-1.5 1.1-2.8 1.9-4zM4.3 14a8 8 0 010-4h3.4a16 16 0 000 4zm.8 2h3a15 15 0 001.3 3.9A8 8 0 015.1 16zm3-8h-3a8 8 0 014.3-3.9A15 15 0 008.1 8zM12 20c-.8-1.2-1.5-2.5-1.9-4h3.8c-.4 1.5-1.1 2.8-1.9 4zm2.3-6H9.7a14 14 0 010-4h4.6a14 14 0 010 4zm.3 5.9a15 15 0 001.3-3.9h3a8 8 0 01-4.3 3.9zm1.7-5.9a16 16 0 000-4h3.4a8 8 0 010 4z"/></svg>www.tlmbespokehomes.com.au</li>
      </ul>
    </div>

    <div class="divider"></div>

    <div class="brand">TLM</div>
    <nav class="social" aria-label="Social links">
      <a class="social__link" href="https://www.tlmbespokehomes.com.au/" aria-label="Social profile"></a>
      <a class="social__link" href="https://www.tlmbespokehomes.com.au/" aria-label="Social profile"></a>
    </nav>
  </section>
</body>
</html>
```